Construction Contractor
Bayt Nuwaris
Professional
Fahad Omar Qurashi
Owner
Rawda Street P.O.Box 483920 Jeddah 24719 Saudi Arabia
baytnuwaris@mailbox-example.com
We need Logo to be in the middle and company name under the logo

```html
<!DOCTYPE html>
<html lang="en">
<head>
<meta charset="utf-8">
<title>Bayt Nuwaris — Business Card</title>
<link href="https://fonts.googleapis.com/css2?family=Montserrat:wght@400;600;700&display=swap" rel="stylesheet">
<style>
  :root {
    --bg: #e9e9e9;
    --card: #ffffff;
    --brown: #5a3a22;
    --gold: #b08d4f;
    --ink-light: #f3ece2;
    --faint: #eeeae4;
    --grey-text: #6a6a6a;
  }
  * { margin: 0; padding: 0; box-sizing: border-box; }
  html, body { width: 1200px; height: 996px; overflow: hidden; }
  body {
    background: var(--bg);
    font-family: "Montserrat", Arial, sans-serif;
    position: relative;
  }
  .card {
    position: absolute;
    left: 290px;
    width: 620px;
    height: 354px;
    background: var(--card);
    border-radius: 18px;
    overflow: hidden;
    box-shadow: 0 6px 18px rgba(0,0,0,0.12);
  }
  .card--back { top: 96px; }
  .card--front { top: 546px; }

  /* back */
  .back-mark {
    position: absolute;
    left: 40px; top: 40px;
    font-size: 64px; font-weight: 700;
    color: var(--faint);
    letter-spacing: 2px;
    text-transform: uppercase;
  }
  .back-web {
    position: absolute;
    right: 40px; bottom: 70px;
    font-size: 15px;
    letter-spacing: 5px;
    color: var(--grey-text);
  }

  /* front */
  .front-shape { position: absolute; inset: 0; }
  .brand {
    position: absolute;
    left: 20px; top: 118px;
    width: 210px;
    display: flex; flex-direction: column; align-items: center; gap: 12px;
  }
  .brand-square {
    width: 46px; height: 46px;
    background: var(--gold);
  }
  .brand-name {
    font-size: 21px; font-weight: 700;
    color: var(--brown);
    text-transform: uppercase;
    letter-spacing: 1px;
    white-space: nowrap;
  }
  .holder {
    position: absolute;
    left: 400px; top: 66px;
  }
  .holder-name {
    font-size: 19px; font-weight: 600;
    color: var(--ink-light);
    white-space: nowrap;
  }
  .holder-role {
    margin-top: 4px;
    font-size: 13px;
    color: var(--gold);
  }
  .contacts {
    position: absolute;
    left: 362px; top: 170px;
    list-style: none;
  }
  .contacts li {
    display: flex; align-items: center; gap: 8px;
    font-size: 10.5px;
    color: var(--ink-light);
    height: 19px;
    white-space: nowrap;
  }
  .contacts .dot {
    width: 11px; height: 11px;
    border-radius: 50%;
    background: var(--ink-light);
    flex: none;
  }
</style>
</head>
<body>

<section class="card card--back">
  <div class="back-mark">Bayt Nuwaris</div>
  <div class="back-web">www.baytnuwaris-example.com</div>
</section>

<section class="card card--front">
  <svg class="front-shape" width="620" height="354" viewBox="0 0 620 354">
    <path d="M380 0 C 330 150, 250 280, 90 354 L620 354 L620 0 Z" fill="var(--brown)"/>
    <path d="M360 0 C 310 150, 230 282, 64 354" fill="none" stroke="var(--gold)" stroke-width="4"/>
  </svg>

  <div class="brand">
    <div class="brand-square"></div>
    <div class="brand-name">Bayt Nuwaris</div>
  </div>

  <div class="holder">
    <div class="holder-name">Fahad Omar Qurashi</div>
    <div class="holder-role">Owner</div>
  </div>

  <ul class="contacts">
    <li><span class="dot"></span>Rawda Street P.O.Box 483920</li>
    <li><span class="dot"></span>Jeddah 24719 Saudi Arabia</li>
    <li><span class="dot"></span>+966 12 555 0142</li>
    <li><span class="dot"></span>+966 55 555 0187</li>
    <li><span class="dot"></span>fahadqurashi</li>
    <li><span class="dot"></span>baytnuwaris@mailbox-example.com</li>
    <li><span class="dot"></span>www.baytnuwaris-example.com</li>
  </ul>
</section>

</body>
</html>
```